Graphic Design Project

I am in need of creating a water bottle label that is clean, simple, Zorvo like, and transparent partially. It most contain the following logo at the top, attached. The address presented may or may not stay. I am looking for something that will remind of water, purity, water droplets. Something nice an clean as refreshing water.

Target Market(s)

Hospital system patients

Industry/Entity Type

Graphic Design

Requirements
Nice to have
• Water drops

Wet

Bluish colors

```html
<!DOCTYPE html>
<html lang="en">
<head>
<meta charset="utf-8">
<title>Hospital Valle Claro – Premium Drinking Water Label</title>
<link rel="stylesheet" href="https://fonts.googleapis.com/css2?family=Tenor+Sans&family=Arimo:wght@700&display=swap">
<style>
  :root {
    --page-bg: #e6eef2;
    --label-silver-light: #f4f6f8;
    --label-silver-mid: #d9dee3;
    --label-silver-dark: #b9c1c8;
    --brand-blue: #1d45a8;
    --brand-green: #3aa84a;
    --band-blue-deep: #0b2f9c;
    --band-blue: #2357d6;
    --splash-deep: #1a3f8a;
    --splash-light: #cfe0ee;
    --text-white: #ffffff;
    --ink-blue: #1b3c9a;
  }
  * { box-sizing: border-box; margin: 0; padding: 0; }
  html, body {
    width: 1200px;
    height: 1000px;
    overflow: hidden;
  }
  body {
    background: var(--page-bg);
    display: flex;
    align-items: center;
    justify-content: center;
  }
  .bottle-label {
    position: relative;
    width: 1000px;
    height: 480px;
    overflow: hidden;
    background: linear-gradient(90deg,
      var(--label-silver-dark) 0%,
      var(--label-silver-light) 22%,
      var(--label-silver-mid) 50%,
      var(--label-silver-light) 78%,
      var(--label-silver-dark) 100%);
    box-shadow: 0 10px 30px rgba(20, 60, 100, 0.18);
  }
  .label-volume {
    position: absolute;
    top: 34px;
    right: 40px;
    font-family: "Arimo", Arial, sans-serif;
    font-weight: 700;
    font-size: 32px;
    color: var(--ink-blue);
  }
  .brand {
    position: absolute;
    top: 50px;
    left: 60px;
    display: flex;
    align-items: center;
    gap: 28px;
  }
  .brand-dot {
    width: 130px;
    height: 130px;
    border-radius: 50%;
    background: var(--brand-blue);
    flex: none;
  }
  .brand-name {
    font-family: "Tenor Sans", "Optima", sans-serif;
    font-weight: 400;
    font-size: 66px;
    line-height: 1.02;
    color: var(--brand-blue);
    text-transform: uppercase;
    letter-spacing: 0.5px;
  }
  .splash-band {
    position: absolute;
    left: 0;
    top: 250px;
    width: 100%;
    height: 120px;
    background: linear-gradient(180deg,
      rgba(207, 224, 238, 0) 0%,
      var(--splash-light) 25%,
      #7f9fc4 60%,
      var(--splash-deep) 100%);
  }
  .product-band {
    position: absolute;
    left: 0;
    bottom: 0;
    width: 100%;
    height: 110px;
    background: linear-gradient(90deg,
      var(--band-blue-deep) 0%,
      var(--band-blue) 50%,
      var(--band-blue-deep) 100%);
    display: flex;
    align-items: center;
    justify-content: center;
  }
  .product-name {
    font-family: "Tenor Sans", "Optima", sans-serif;
    font-size: 60px;
    color: var(--text-white);
    letter-spacing: 0.5px;
  }
</style>
</head>
<body>
  <main class="bottle-label">
    <div class="label-volume">16.9 fl oz (500mL)</div>
    <div class="brand">
      <span class="brand-dot" aria-hidden="true"></span>
      <h1 class="brand-name">Hospital<br>Valle Claro</h1>
    </div>
    <div class="splash-band" role="img" aria-label="Photograph of a splashing clear water surface"></div>
    <div class="product-band">
      <p class="product-name">Premium Drinking Water</p>
    </div>
  </main>
</body>
</html>
```